Fun Trendy High End Spa Services
Business Card, Gift Certificate, Gift Certificate Envelope
I need double sided standard sized Business Card [3.5" x 2"]
We like what is in logo that was uploaded but please use your creativity. We are open to any ideas.
Simple
Lena Harbus LMT
Owner
Mobile
BP@BrightPebblo.com
BrightPebblo.com
We are open to all concepts. So please be creative. This is for Very high end spa service so it needs to look very good. We thought black paper for a base on business cards, gift certificate and GC envelope but are open to any and all ideas! Thank You! We will pick a winner early if we find the perfect design.
"The greatest wealth is health"
(Doesnt need " " on there just use your own idea and play with it.)
Here is The winning logo design. We really like the style but please feel free to be creative with it! Thank you so much!
This is the style of gift certificate that we want designed to match our business card.

```html
<!DOCTYPE html>
<html lang="en">
<head>
<meta charset="utf-8">
<title>Bright Pebblo – Business Card</title>
<link rel="stylesheet" href="https://fonts.googleapis.com/css2?family=Open+Sans:ital,wght@0,300;0,400;0,700;1,700&display=swap">
<style>
  :root {
    --page: #ecebe8;
    --card-dark: #0d0d0d;
    --card-mid: #3a3a3a;
    --silver-light: #f4f4f4;
    --silver-mid: #c9c9c9;
    --silver-dark: #9a9a9a;
    --ink-dark: #1a1a1a;
    --ink-light: #ffffff;
    --mark: #d8d8d8;
  }
  * { margin: 0; padding: 0; box-sizing: border-box; }
  html, body { width: 1200px; height: 937px; overflow: hidden; }
  body {
    background: var(--page);
    font-family: "Open Sans", Arial, sans-serif;
    position: relative;
  }
  .card {
    position: absolute;
    background: radial-gradient(ellipse at 45% 50%, var(--card-mid) 0%, var(--card-dark) 75%);
    box-shadow: 0 6px 16px rgba(0,0,0,0.25);
    overflow: hidden;
  }
  .card-front { left: 106px; top: 101px; width: 671px; height: 347px; }
  .card-back  { left: 486px; top: 494px; width: 603px; height: 341px; }
  .card-shapes { position: absolute; inset: 0; width: 100%; height: 100%; }

  .tagline {
    position: absolute; left: 26px; top: 22px;
    color: var(--ink-light); font-style: italic; font-weight: 700; font-size: 14px;
  }
  .contact-name {
    position: absolute; right: 24px; top: 18px; text-align: right;
    color: var(--ink-dark); font-weight: 700; font-size: 22px; line-height: 1.1;
  }
  .contact-role {
    display: block; font-weight: 400; font-size: 15px; color: #444;
  }
  .brand {
    position: absolute; display: flex; align-items: center; gap: 18px;
    color: var(--mark); font-weight: 300;
  }
  .brand-dot {
    border: 3px solid var(--mark); border-radius: 50%;
  }
  .card-front .brand { left: 120px; top: 128px; font-size: 44px; }
  .card-front .brand-dot { width: 66px; height: 66px; }
  .website {
    position: absolute; left: 28px; bottom: 20px;
    color: var(--ink-dark); font-weight: 700; font-size: 16px;
  }
  .phone {
    position: absolute; right: 24px; bottom: 18px; text-align: right;
    color: var(--ink-light); font-size: 14px; line-height: 1.35;
  }
  .motto {
    position: absolute; left: 24px; top: 16px;
    color: var(--ink-light); font-style: italic; font-weight: 700; font-size: 22px;
  }
  .card-back .brand { left: 50%; top: 50%; transform: translate(-50%, -50%); font-size: 34px; }
  .card-back .brand-dot { width: 60px; height: 60px; }
</style>
</head>
<body>
  <section class="card card-front">
    <svg class="card-shapes" viewBox="0 0 671 347" preserveAspectRatio="none" aria-hidden="true">
      <defs>
        <linearGradient id="silverFront" x1="0" y1="0" x2="1" y2="1">
          <stop offset="0" stop-color="var(--silver-dark)"/>
          <stop offset="0.45" stop-color="var(--silver-light)"/>
          <stop offset="1" stop-color="var(--silver-mid)"/>
        </linearGradient>
      </defs>
      <path d="M273,0 C430,0 500,70 671,80 L671,0 Z" fill="url(#silverFront)"/>
      <path d="M0,240 C130,245 260,285 400,347 L0,347 Z" fill="url(#silverFront)"/>
    </svg>
    <p class="tagline">Your premier in home spa service provider</p>
    <p class="contact-name">Lena Harbus LMT<span class="contact-role">Owner</span></p>
    <div class="brand"><span class="brand-dot"></span><span>Bright Pebblo</span></div>
    <p class="website">www.BrightPebblo.com</p>
    <p class="phone">Mobile<br>Ph 555-014-2290</p>
  </section>

  <section class="card card-back">
    <svg class="card-shapes" viewBox="0 0 603 341" preserveAspectRatio="none" aria-hidden="true">
      <defs>
        <linearGradient id="silverBack" x1="0" y1="0" x2="1" y2="1">
          <stop offset="0" stop-color="var(--silver-dark)"/>
          <stop offset="0.45" stop-color="var(--silver-light)"/>
          <stop offset="1" stop-color="var(--silver-mid)"/>
        </linearGradient>
      </defs>
      <path d="M273,0 C410,0 470,75 603,88 L603,0 Z" fill="url(#silverBack)"/>
      <path d="M0,215 C130,225 270,270 400,341 L0,341 Z" fill="url(#silverBack)"/>
    </svg>
    <p class="motto">The greatest wealth is health</p>
    <div class="brand"><span class="brand-dot"></span><span>Bright Pebblo</span></div>
  </section>
</body>
</html>
```